www.BrightCoveSmileStudio.com needs to be re-designed

Current website to be redesigned www.BrightCoveSmileStudio.com

*Need a custom-made new theme

I need all 10 pages redesigned using existing content.
I need the website to be revamped to a more modern look.

Please start with Homepage first then after homepage mock up is approved we can move forward with rest of pages.

Please use existing images from my Facebook or Instagram page of our real customers for banner image...

(Where to find my FB and IG pages...
You can access these pages from the website header and "contact us" page for address.)

I would like to have a button that says "Book Appointment Online" and get rid of the actual form that is on current website.

But other than that please include all other content, features, etc in mock ups so I can make a decision on the website.

I prefer custom design and must be WP installable responsive theme.

This is design-only. I am open to any concepts you can submit.

Target Market(s)

people that care about thier looks

Industry/Entity Type

Dental Clinic

Colors

Designer to choose colors to be used in the design.

Requirements
Must have
• All current content/text that is currently on website. Just formatted so it doesnt look so busy. I want to make emphasis on BOOK APPOINTMENT button and $99 SPECIAL BUTTON
Nice to have
• White background so everything pops
Should not have
• I do not like stock photo images, please use images from my facebook and IG page of real customers or even a snap shot of our office building. You can access these pages from the website header and contact us page for address, maybe yu can use snapshot somewhere of building of our address on homepage possibly in banner image.

```html
<!DOCTYPE html>
<html lang="en">
<head>
<meta charset="utf-8">
<title>Bright Cove Smile Studio</title>
<link rel="stylesheet" href="https://fonts.googleapis.com/css2?family=Ubuntu:wght@400;500;700&family=Open+Sans:wght@400;600&display=swap">
<style>
:root{
  --blue:#00a9d6;
  --blue-dark:#0096c2;
  --band-a:#17b0d2;
  --band-b:#3cc3de;
  --ink:#222;
  --text:#7a7a7a;
  --soft:#f1f1f1;
  --navy:#2b3a55;
  --white:#fff;
}
*{margin:0;padding:0;box-sizing:border-box}
html,body{width:1200px;height:3291px;overflow:hidden;background:var(--white)}
body{position:relative;font-family:"Open Sans",sans-serif;color:var(--text)}
.abs{position:absolute}
.heading{font-family:"Ubuntu",sans-serif;font-weight:500;color:var(--ink);text-align:center}
.btn-outline{position:absolute;display:flex;align-items:center;justify-content:center;border:2px solid var(--blue);color:var(--blue);font-family:"Ubuntu",sans-serif;font-size:19px;background:var(--white)}
.btn-solid{position:absolute;display:flex;align-items:center;justify-content:center;background:var(--blue);color:var(--white);font-family:"Ubuntu",sans-serif;font-weight:500;font-size:15px;text-transform:uppercase}

/* header */
.brand{left:99px;top:26px;display:flex;align-items:center;gap:14px}
.brand-mark{width:70px;height:70px;border-radius:50%;background:#dde5ea}
.brand-name{font-family:"Ubuntu",sans-serif;font-weight:500;font-size:27px;color:var(--navy)}
.call{left:516px;top:42px;display:flex;align-items:center;gap:12px;font-family:"Ubuntu",sans-serif;font-size:21px;color:var(--ink)}
.call b{font-weight:700}
.book{left:853px;top:42px;width:248px;height:40px;font-size:14px}
.nav{left:0;top:120px;width:1200px;height:62px;background:var(--blue)}
.nav a{position:absolute;top:23px;color:var(--white);font-family:"Ubuntu",sans-serif;font-weight:500;font-size:12.5px;text-decoration:none;text-transform:uppercase}

/* hero */
.hero{left:0;top:182px;width:1200px;height:619px;background:linear-gradient(90deg,#eef0f2 0%,#d9c9b6 30%,#cfb9a3 55%,#e7ded3 80%,#f3f3f3 100%)}
.special{left:529px;top:531px;width:272px;height:176px;border-radius:50%;background:var(--blue);border:6px solid var(--white);color:var(--white);font-family:"Ubuntu",sans-serif;text-align:center;box-shadow:0 4px 10px rgba(0,0,0,.15)}
.special .price{font-size:66px;font-weight:700;line-height:1;margin-top:26px}
.special .label{font-size:22px;font-weight:500}
.arrow{top:434px;width:44px;height:44px;border-radius:50%;background:rgba(255,255,255,.6)}

/* intro */
.intro-title{left:0;top:888px;width:1200px;font-size:40px}
.intro-text{left:171px;top:952px;width:860px;font-size:13px;line-height:25px;text-align:center}
.intro-text p+p{margin-top:24px}

/* why */
.why{left:0;top:1261px;width:1200px;height:356px;background:linear-gradient(120deg,var(--band-a),var(--band-b) 60%,var(--band-a))}
.why-title{left:0;top:1310px;width:1200px;font-size:40px;color:var(--white);font-weight:700}
.feature{top:1396px;width:200px;text-align:center;color:var(--white);font-family:"Ubuntu",sans-serif;font-weight:500;font-size:23px}
.feature .ring{width:118px;height:118px;margin:0 auto 18px;border:2px solid var(--white);border-radius:50%;display:flex;align-items:center;justify-content:center}

/* how */
.how-title{left:0;top:1686px;width:1200px;font-size:40px;font-weight:700}
.how-text{left:99px;top:1772px;width:540px;font-size:13px;line-height:26px}
.how-text p+p{margin-top:12px}
.video{left:669px;top:1773px;width:437px;height:283px;border:1px solid #ddd;background:var(--white);box-shadow:0 1px 4px rgba(0,0,0,.12);padding:10px}
.video-frame{position:relative;width:100%;height:100%;background:linear-gradient(135deg,#2d3e52,#5a4b66 55%,#1d2430)}

/* treatments */
.treat{left:0;top:2133px;width:1200px;height:346px;background:var(--soft)}
.ba-label{top:2204px;font-family:"Ubuntu",sans-serif;font-size:23px;color:#333}
.ba{left:99px;top:2233px;width:384px;height:169px;border:3px solid var(--white);background:linear-gradient(90deg,#d9a38e 0%,#e9c9a4 49.5%,#f6ece6 50.5%,#e7a795 100%)}
.treat-title{left:575px;top:2212px;font-size:29px;font-weight:700;text-align:left}
.treat-text{left:575px;top:2263px;width:540px;font-size:13px;line-height:24px}

/* testimonials */
.test-title{left:0;top:2548px;width:1200px;font-size:40px}
.quote{left:226px;top:2634px;width:748px;text-align:center;font-size:18px;line-height:24px;color:#666}
.qmark{font-family:Georgia,serif;font-size:64px;color:#d4d4d4;line-height:1}
.avatar{left:559px;top:2727px;width:80px;height:80px;border-radius:50%;border:4px solid var(--white);box-shadow:0 0 0 1px #ddd;background:linear-gradient(#c9b29a,#8c7360)}
.author{left:0;top:2826px;width:1200px;text-align:center;font-family:"Ubuntu",sans-serif;font-weight:700;font-size:18px;color:var(--blue)}

/* footer */
.footer{left:0;top:2951px;width:1200px;height:340px;background:var(--blue);color:var(--white)}
.f-head{top:2991px;font-family:"Ubuntu",sans-serif;font-weight:500;font-size:17px;text-transform:uppercase;color:var(--white)}
.f-list{top:3030px;font-size:14px;line-height:31.5px;color:var(--white)}
.f-list svg{vertical-align:-2px;margin-right:6px}
.email{left:774px;top:3061px;width:222px;height:39px;background:var(--white);color:#aaa;font-size:12px;padding:12px 16px;letter-spacing:.5px}
.subscribe{left:996px;top:3061px;width:105px;height:39px;background:#111;color:var(--white);font-family:"Ubuntu",sans-serif;font-weight:500;font-size:13px;display:flex;align-items:center;justify-content:center}
.social{top:3113px;width:40px;height:40px;border-radius:50%;background:var(--white)}
.rule{left:99px;top:3218px;width:1002px;height:1px;background:rgba(255,255,255,.5)}
.copy{left:99px;top:3241px;font-size:13px;color:var(--white)}
</style>
</head>
<body>

<!-- Header -->
<div class="abs brand">
  <div class="brand-mark"></div>
  <div class="brand-name">Bright Cove Smile Studio</div>
</div>
<div class="abs call">
  <svg width="40" height="40" viewBox="0 0 40 40"><circle cx="20" cy="20" r="18" fill="none" stroke="#00a9d6" stroke-width="2.5"/><path d="M14 11c1-1 2-1 3 0l2 3c.6 1 .4 2-.4 2.7l-1.2 1c.9 2.4 2.6 4.1 5 5l1-1.2c.7-.8 1.7-1 2.7-.4l3 2c1 1 1 2 0 3l-1.4 1.4c-1.4 1.4-4 1.2-7-.8-3.3-2.2-6-5-8-8.3-1.8-3-2-5.3-.6-6.8z" fill="#00a9d6"/></svg>
  <span>CALL NOW: <b>555-014-2297</b></span>
</div>
<div class="btn-solid book">Book Appointment Online</div>

<nav class="abs nav">
  <a style="left:118px">Home</a>
  <a style="left:191px">Our Process</a>
  <a style="left:312px">Photos</a>
  <a style="left:397px">White Smile Club</a>
  <a style="left:544px">Testimonials</a>
  <a style="left:667px">Appointments</a>
  <a style="left:799px">FAQ</a>
  <a style="left:858px">Contact</a>
  <a style="left:952px">Blog</a>
  <a style="left:1020px">Buy Now</a>
</nav>

<!-- Hero -->
<div class="abs hero" role="img" aria-label="Photo of three smiling studio customers and staff in front of a branded backdrop"></div>
<div class="abs arrow" style="left:14px"></div>
<div class="abs arrow" style="left:1134px"></div>
<div class="abs special"><div class="price">$99</div><div class="label">SPECIAL</div></div>
<svg class="abs" style="left:0;top:796px" width="1200" height="40" viewBox="0 0 1200 40">
  <path d="M120 16 Q600 40 1080 14 Q600 30 120 16Z" fill="#00a9d6"/>
</svg>

<!-- Intro -->
<h1 class="abs heading intro-title">Bright Cove Smile Studio</h1>
<div class="abs intro-text">
  <p>Bright Cove Smile Studio features state-of-the-art technologies that are safe, industry-unique and very cost-effective. Our teeth whitening system utilizes the latest blue light whitening technology. Our Blue Light Systems are calibrated precisely for optimal activation of our exclusive hydrogen peroxide based whitening solution which is manufactured in a FDA registered facility in the USA.</p>
  <p>Our special lighting systems intensify the release of hydroxyl radicals that accelerate the dissipation of tooth stains. The entire teeth whitening process is accelerated and able to be completed in just 45 minutes with instant results.</p>
</div>
<div class="btn-outline" style="left:459px;top:1145px;width:283px;height:51px">READ MORE INFORMATION</div>

<!-- Why choose us -->
<div class="abs why"></div>
<h2 class="abs heading why-title">Why Choose Us?</h2>
<div class="abs feature" style="left:58px"><div class="ring">
  <svg width="56" height="56" viewBox="0 0 56 56"><path d="M28 10h16v16L24 46 8 30z" fill="#fff"/><circle cx="37" cy="17" r="3.5" fill="#2bb9d9"/><path d="M39 13c4-6 10-3 8 2" stroke="#fff" stroke-width="2.5" fill="none"/></svg>
</div>Price</div>
<div class="abs feature" style="left:277px"><div class="ring">
  <svg width="56" height="56" viewBox="0 0 56 56"><rect x="14" y="10" width="28" height="38" rx="3" fill="none" stroke="#fff" stroke-width="3"/><rect x="22" y="6" width="12" height="8" rx="2" fill="#fff"/><path d="M19 24l3 3 5-6M31 24h7M19 35l3 3 5-6M31 35h7" stroke="#fff" stroke-width="2.5" fill="none"/></svg>
</div>Results</div>
<div class="abs feature" style="left:495px"><div class="ring">
  <svg width="56" height="56" viewBox="0 0 56 56"><path d="M16 8c5-2 8 2 12 2s7-4 12-2c6 3 5 12 3 18-2 7-2 22-7 22-4 0-3-14-8-14s-4 14-8 14c-5 0-5-15-7-22-2-6-3-15 3-18z" fill="#fff"/></svg>
</div>No Pain</div>
<div class="abs feature" style="left:714px"><div class="ring">
  <svg width="56" height="56" viewBox="0 0 56 56"><circle cx="34" cy="12" r="5" fill="#fff"/><path d="M12 28l14 6 12-4 8 6-4 4-6-4-12 4-14-6zM24 40v8M18 48h14" stroke="#fff" stroke-width="3" fill="none"/><path d="M28 18l8 2-2 10-6 2z" fill="#fff"/></svg>
</div>Service</div>
<div class="abs feature" style="left:933px"><div class="ring">
  <svg width="56" height="56" viewBox="0 0 56 56"><rect x="10" y="26" width="8" height="20" fill="#fff"/><path d="M21 26l8-14c2-3 6-2 6 2l-2 9h11c3 0 4 3 3 5l-4 15c-1 2-2 3-4 3H21z" fill="#fff"/></svg>
</div>Convenience</div>

<!-- How it works -->
<h2 class="abs heading how-title">HOW IT WORKS</h2>
<div class="abs how-text">
  <p>We have a very effective teeth whitening treatment that is guaranteed to get you quick results in about 1 hour. To start the treatment you'll apply a Hydrogen Peroxide based whitening agent to your teeth. We then place our cold blue light directly in front of your exposed teeth for 15 minutes per treatment. The lighting systems we use activate the whitening agent and thats what accelerates the whitening process, giving you whiter teeth in less than an hour.</p>
  <p>We always perform what we call a "Triple Treatment". So that's 3 of the 15 minute treatments all done consecutively.</p>
</div>
<div class="btn-solid" style="left:99px;top:2005px;width:234px;height:51px;font-size:14px">Free Whitening For Life</div>
<div class="abs video">
  <div class="video-frame" role="img" aria-label="Video still of a customer receiving blue light whitening treatment">
    <svg style="position:absolute;left:0;top:0" width="415" height="261" viewBox="0 0 415 261">
      <circle cx="207" cy="120" r="34" fill="rgba(0,0,0,.25)" stroke="#fff" stroke-width="3"/>
      <path d="M197 104v32l26-16z" fill="#fff"/>
      <rect x="0" y="238" width="415" height="23" fill="#111"/>
      <path d="M10 244v11l9-5.5z" fill="#fff"/>
      <rect x="30" y="248" width="330" height="4" rx="2" fill="#555"/>
      <rect x="30" y="248" width="120" height="4" rx="2" fill="#2aa4d0"/>
      <path d="M378 246h4l5-4v16l-5-4h-4z" fill="#fff"/>
    </svg>
  </div>
</div>

<!-- Treatments -->
<div class="abs treat"></div>
<div class="abs ba-label" style="left:157px">Before</div>
<div class="abs ba-label" style="left:352px">After</div>
<div class="abs ba" role="img" aria-label="Before and after close-up of a smile, stained teeth on the left and whitened teeth on the right"></div>
<h2 class="abs heading treat-title">BRIGHT COVE TREATMENTS</h2>
<div class="abs treat-text">Our special lighting systems intensify the release of hydroxyl radicals that accelerate the dissipation of tooth stains. The entire teeth whitening process is accelerated and able to be completed in just 45 minutes with instant results.</div>
<div class="btn-outline" style="left:575px;top:2354px;width:237px;height:48px;font-size:14px;border-width:1px">FREE WHITENING FOR LIFE</div>

<!-- Testimonials -->
<h2 class="abs heading test-title">Testimonials</h2>
<div class="abs qmark" style="left:176px;top:2618px">&ldquo;</div>
<div class="abs quote">Great customer service and great results!! I had my teeth whitened here and loved the results! I have tried a couple different places in the past and didn't have the best of results being a coffee drinker and a smoker. I will definitely be a returning customer!</div>
<div class="abs qmark" style="left:985px;top:2672px">&rdquo;</div>
<div class="abs avatar" role="img" aria-label="Portrait of the reviewing customer"></div>
<div class="abs author">Maya L. Bayside</div>
<svg class="abs" style="left:574px;top:2866px" width="52" height="14" viewBox="0 0 52 14">
  <circle cx="7" cy="7" r="5" fill="none" stroke="#00a9d6" stroke-width="1.5"/>
  <circle cx="26" cy="7" r="5.5" fill="#00a9d6"/>
  <circle cx="45" cy="7" r="5.5" fill="#00a9d6"/>
</svg>

<!-- Footer -->
<footer class="abs footer"></footer>
<div class="abs f-head" style="left:99px">Opening Hours</div>
<div class="abs f-list" style="left:99px">Monday to Friday<br>9am-5pm<br>Saturday<br>10am-2pm</div>
<div class="abs f-list" style="left:279px">Terms &amp; Conditions<br>Privacy Policy<br>Site Map<br>Appointment</div>
<div class="abs f-head" style="left:461px">Contact Address</div>
<div class="abs f-list" style="left:461px">
  480 Harbor View Road<br>
  Suite 12 Bayside, CA 90000<br>
  <svg width="14" height="14" viewBox="0 0 14 14"><rect width="14" height="14" rx="2" fill="#fff"/><path d="M4 3l2 2-1 1.5c.6 1.2 1.3 1.9 2.5 2.5L9 8l2 2-1.5 1.5C6.5 11 3 7.5 2.5 4.5z" fill="#00a9d6"/></svg>555-018-3306<br>
  <svg width="14" height="12" viewBox="0 0 14 12"><rect width="14" height="12" rx="1.5" fill="#fff"/><path d="M1 2l6 5 6-5" stroke="#00a9d6" stroke-width="1.4" fill="none"/></svg>hello@brightcovesmile.com
</div>
<div class="abs f-head" style="left:774px">Sign up for Newsletters</div>
<div class="abs f-list" style="left:774px;top:3024px;font-size:13px">Please sign up here for latest news</div>
<div class="abs email">EMAIL ADDRESS</div>
<div class="abs subscribe">SUBSCRIBE</div>
<div class="abs social" style="left:774px" aria-label="Social profile"></div>
<div class="abs social" style="left:825px" aria-label="Social profile"></div>
<div class="abs social" style="left:873px" aria-label="Social profile"></div>
<div class="abs social" style="left:921px" aria-label="Social profile"></div>
<div class="abs rule"></div>
<div class="abs copy">&copy; 2017 BRIGHT COVE SMILE STUDIO. All right reserved . Term of Use</div>

</body>
</html>
```